Audit/Compliance company needs Business Card Template

We are after a Business Card Template that we can modify internally to update details as people change positions.
We are an Australian based company specalising in Auditing and Quality/OHS systems development. - See www.keelbrookmeridian.com.au for more information
We would like the desings to be based around our logo and colours assocaited with it (attached for your information) however we are very open as to how the cards are designed.
We are looking for something quite edgy and mordern but it must have a professional/compliance feel to it (if possible).
The main details we would like to include within the card template are:
Name
Position Title
Postal Address
Phone Number
Mobile Number
Email Address
Website
The cards will be printed through folio mint on Glossy paper so it should reflect the requirements below
Full Bleed Size (starting document size)
90 x 52 mm
1062 x 615 pixels
Document Trim Size (final size after being cut)
87 x 49 mm
1028 x 579 pixels
Resolution
300 DPI

```html
<!DOCTYPE html>
<html lang="en">
<head>
<meta charset="utf-8">
<title>Keelbrook Meridian – Business Card</title>
<link rel="stylesheet" href="https://fonts.googleapis.com/css2?family=Barlow:wght@400;500;700&display=swap">
<style>
  :root {
    --bg: #ededed;
    --card: #ffffff;
    --frame: #d4d4d4;
    --orange: #f26a2e;
    --navy: #1d4f73;
    --grey-text: #5a5a5a;
    --rule: #b8b8b8;
  }
  * { margin: 0; padding: 0; box-sizing: border-box; }
  html, body { width: 1200px; height: 1000px; overflow: hidden; }
  body {
    background: var(--bg);
    font-family: "Barlow", Arial, sans-serif;
    position: relative;
  }
  .card {
    position: absolute;
    left: 220px;
    width: 760px;
    height: 428px;
    background: var(--card);
    box-shadow: 0 6px 20px rgba(0,0,0,0.12);
  }
  .card-back { top: 50px; }
  .card-front { top: 522px; }

  /* back side */
  .inner-frame {
    position: absolute;
    inset: 12px;
    border: 2px solid var(--frame);
  }
  .back-brand {
    position: absolute;
    left: 0; right: 0; top: 150px;
    display: flex;
    align-items: center;
    justify-content: center;
    gap: 16px;
  }
  .brand-square {
    width: 46px; height: 46px;
    background: var(--orange);
  }
  .brand-name {
    font-weight: 500;
    font-size: 34px;
    letter-spacing: 2px;
    color: var(--grey-text);
    text-transform: uppercase;
  }
  .back-band {
    position: absolute;
    left: 14px; right: 14px;
    top: 318px;
    height: 16px;
    background: var(--orange);
    border-top: 3px solid #fff;
    border-bottom: 3px solid #fff;
    outline: 1px solid var(--frame);
  }

  /* front side */
  .front-logo {
    position: absolute;
    left: 70px; top: 44px;
    display: flex; align-items: center; gap: 12px;
  }
  .front-logo .brand-square { width: 34px; height: 34px; }
  .front-logo .brand-name { font-size: 24px; color: var(--navy); letter-spacing: 1px; }
  .divider {
    position: absolute;
    left: 0; top: 0;
  }
  .contact {
    position: absolute;
    left: 440px; top: 128px;
    width: 300px;
  }
  .person-name {
    font-weight: 700;
    font-size: 26px;
    color: var(--navy);
    padding-bottom: 4px;
    border-bottom: 2px solid var(--navy);
  }
  .person-role {
    font-size: 15px;
    color: var(--orange);
    margin-top: 4px;
  }
  .details {
    list-style: none;
    margin-top: 36px;
    font-size: 13px;
    color: var(--grey-text);
    line-height: 1.45;
  }
  .details li { display: flex; gap: 7px; align-items: flex-start; }
  .details li.indent { padding-left: 17px; }
  .icon { width: 10px; height: 10px; margin-top: 4px; flex: none; }
  .website {
    position: absolute;
    left: 440px; top: 318px;
    font-weight: 700;
    font-size: 16px;
    color: var(--orange);
  }
  .front-band {
    position: absolute;
    left: 0; right: 0;
    top: 346px;
    height: 22px;
    background: var(--orange);
  }
  .front-band-thin {
    position: absolute;
    left: 0; right: 0;
    top: 372px;
    height: 3px;
    background: var(--orange);
  }
</style>
</head>
<body>

<section class="card card-back" aria-label="Business card back">
  <div class="inner-frame"></div>
  <div class="back-brand">
    <span class="brand-square"></span>
    <span class="brand-name">Keelbrook Meridian</span>
  </div>
  <div class="back-band"></div>
</section>

<section class="card card-front" aria-label="Business card front">
  <div class="front-logo">
    <span class="brand-square"></span>
    <span class="brand-name">Keelbrook Meridian</span>
  </div>

  <svg class="divider" width="760" height="428" aria-hidden="true">
    <line x1="320" y1="300" x2="430" y2="120" stroke="var(--rule)" stroke-width="1.5"/>
  </svg>

  <div class="contact">
    <h1 class="person-name">Mr. Alex Marlow</h1>
    <p class="person-role">Manager</p>
    <ul class="details">
      <li><svg class="icon" viewBox="0 0 10 10"><rect width="10" height="10" rx="1.5" fill="var(--orange)"/><path d="M2 3.5h6v3.5H2z M2 3.5l3 2 3-2" fill="none" stroke="#fff" stroke-width="0.9"/></svg>audit@keelbrookmeridian.com.au</li>
      <li><svg class="icon" viewBox="0 0 10 10"><rect width="10" height="10" rx="1.5" fill="var(--orange)"/><path d="M5 8.2L3 5a2 2 0 1 1 4 0z" fill="#fff"/></svg>Suite 4, 118 Harrow Lane,</li>
      <li class="indent">Brenton VIC 3999</li>
      <li><svg class="icon" viewBox="0 0 10 10"><rect width="10" height="10" rx="1.5" fill="var(--orange)"/><path d="M3 2.2l1.2 1.6-.7.8a4 4 0 0 0 1.9 1.9l.8-.7 1.6 1.2-.8 1A5 5 0 0 1 2 3z" fill="#fff"/></svg>03 5550 1410</li>
      <li><svg class="icon" viewBox="0 0 10 10"><rect width="10" height="10" rx="1.5" fill="var(--orange)"/><rect x="2.5" y="2.5" width="5" height="5" fill="none" stroke="#fff" stroke-width="0.9"/></svg>03 5550 1420</li>
    </ul>
  </div>

  <p class="website">www.keelbrookmeridian.com.au</p>
  <div class="front-band"></div>
  <div class="front-band-thin"></div>
</section>

</body>
</html>
```